Recruitment Flyer for Harbourline Home Loan company

Harbourline Home Loan centre requires a four page A4 color brochure for new staff who will be joining the organisation.

The brochure is received during the interview for the job role. so we are looking for nice glossy pictures combined with sufficient text to enable the applicant to make an informed decision.

I have attached a word document that may help plus lots of pictures that are on the website that could be used also.

Target Market(s)

New staff joining the organisation

Industry/Entity Type

Mortgage

Font styles to use
Sans Serif

Colors
3377b5
6b449b
b768aa
34a6d7

Requirements
Must have
• Glossy, colorful and career happy
Nice to have
• lots of photos and opportunity for text
Should not have
• be sad or not happy

```html
<!DOCTYPE html>
<html lang="en">
<head>
<meta charset="utf-8">
<title>Harbourline Home Loan Centre – Recruitment Brochure</title>
<link href="https://fonts.googleapis.com/css2?family=Montserrat:ital,wght@0,700;0,800;1,500&family=Lato:ital,wght@0,400;1,400&family=Tinos:wght@700&family=Arimo:wght@400&display=swap" rel="stylesheet">
<style>
  :root{
    --blue:#14a0e3;
    --purple:#6b449b;
    --ink:#1c1c1c;
    --grey:#4a4a4a;
    --paper:#ffffff;
    --backdrop:#e9e9ec;
  }
  *{box-sizing:border-box;margin:0;padding:0}
  html,body{width:1200px;height:1200px;overflow:hidden;background:var(--backdrop)}
  .spread{position:absolute;left:40px;top:204px;width:1120px;height:792px;display:flex}
  .page{position:relative;width:560px;height:792px;background:var(--paper);overflow:hidden}
  .page + .page{border-left:1px solid #e2e2e2}
  .page-shapes{position:absolute;inset:0;width:560px;height:792px}

  /* back cover */
  .facilities{position:absolute;right:44px;top:44px;text-align:right}
  .facilities h2{font:800 22px/1 "Montserrat",sans-serif;color:var(--blue);margin-bottom:12px}
  .facilities li{list-style:none;font:italic 500 12px/1 "Montserrat",sans-serif;color:var(--ink);margin-bottom:12px}
  .facilities li::after{content:"";display:inline-block;width:10px;height:6px;border-radius:50%;margin-left:8px;background:var(--blue);vertical-align:middle}
  .facilities li:nth-child(even)::after{background:var(--purple)}
  .photo-meeting{position:absolute;left:26px;top:146px;width:196px;height:196px;border-radius:50%;
    background:radial-gradient(circle at 40% 35%,#c9ced6,#7f8a98 60%,#4b4f58);border:8px solid var(--blue)}
  .call{position:absolute;left:300px;top:300px}
  .call h3{font:800 22px/1 "Montserrat",sans-serif;color:var(--blue)}
  .call p{font:800 24px/1.1 "Montserrat",sans-serif;color:var(--ink);letter-spacing:1px;margin-top:4px}
  .body-copy{position:absolute;left:50px;top:398px;width:440px;font:italic 400 11.5px/1.3 "Lato",sans-serif;color:var(--ink)}
  .body-copy p{margin-bottom:14px}
  .back-footer{position:absolute;left:44px;right:36px;top:648px;display:flex;justify-content:space-between;align-items:center;color:#fff}
  .website{font:700 20px/1 "Tinos",serif;display:flex;align-items:center;gap:8px}
  .website::before{content:"";width:13px;height:13px;border-radius:50%;border:2px solid #fff}

  /* brand name block */
  .brand{display:flex;align-items:center;gap:10px}
  .brand-dot{width:34px;height:34px;border-radius:50%;background:currentColor}
  .brand-name{font:700 15px/1.15 "Montserrat",sans-serif;letter-spacing:1.5px;text-transform:uppercase}
  .brand--light{color:#fff}
  .brand--light .brand-dot{width:26px;height:26px}
  .brand--light .brand-name{font-size:12px}
  .brand--cover{position:absolute;left:80px;top:40px;color:var(--blue)}

  /* front cover */
  .photo-team{position:absolute;left:0;top:120px;width:560px;height:320px}
  .headline{position:absolute;left:0;right:0;top:470px;text-align:center}
  .headline .line-1{display:block;font:700 92px/1 "Tinos",serif;color:var(--grey);letter-spacing:1px}
  .headline .line-2{display:block;font:400 76px/1 "Arimo",sans-serif;color:var(--blue);margin-top:-4px}
</style>
</head>
<body>
<main class="spread">

  <section class="page back-cover">
    <svg class="page-shapes" viewBox="0 0 560 792" aria-hidden="true">
      <path d="M340 4 Q210 40 160 150" fill="none" stroke="var(--purple)" stroke-width="6"/>
      <path d="M60 330 L0 356" fill="none" stroke="var(--purple)" stroke-width="2"/>
      <path d="M228 222 Q400 198 560 206 L560 226 Q400 220 226 244 Z" fill="var(--purple)"/>
      <path d="M0 600 Q300 660 560 560 L560 752 L0 762 Z" fill="var(--blue)"/>
    </svg>

    <div class="facilities">
      <h2>Facilities</h2>
      <ul>
        <li>Lorem ipsum dolor sit amet.</li>
        <li>Praesent egestas mauris sit amet.</li>
        <li>Phasellus ultrices magna quis.</li>
        <li>Donec elementum justo ut elit.</li>
        <li>Sed laoreet arcu eget luctus.</li>
      </ul>
    </div>

    <div class="photo-meeting" role="img" aria-label="Photo: two colleagues reviewing paperwork at an office desk"></div>

    <div class="call">
      <h3>Call us on.</h3>
      <p>XXX-XXXX-XX</p>
    </div>

    <div class="body-copy">
      <p>Lorem Ipsum is simply dummy text of the printing and typesetting industry. Lorem Ipsum has been the industry's standard dummy text ever since the 1500s, when an unknown printer took a galley of type and scrambled it to make a type specimen book.</p>
      <p>Lorem Ipsum is simply dummy text of the printing and typesetting industry. Lorem Ipsum has been the industry's standard dummy text ever since.</p>
    </div>

    <footer class="back-footer">
      <span class="website">harbourlinehomeloan.com</span>
      <div class="brand brand--light">
        <span class="brand-dot"></span>
        <span class="brand-name">Harbourline<br>Home Loan Centre</span>
      </div>
    </footer>
  </section>

  <section class="page front-cover">
    <svg class="page-shapes" viewBox="0 0 560 792" aria-hidden="true">
      <path d="M0 742 Q280 748 560 736 L560 762 L0 770 Z" fill="var(--purple)"/>
    </svg>

    <div class="brand brand--cover">
      <span class="brand-dot"></span>
      <span class="brand-name">Harbourline<br>Home Loan Centre</span>
    </div>

    <svg class="photo-team" viewBox="0 120 560 320" role="img" aria-label="Photo: cheerful team of colleagues raising their arms in celebration">
      <defs>
        <linearGradient id="team-tones" x1="0" y1="0" x2="1" y2="1">
          <stop offset="0" stop-color="#d7dde4"/>
          <stop offset="0.5" stop-color="#b79a86"/>
          <stop offset="1" stop-color="#5c6a55"/>
        </linearGradient>
      </defs>
      <path d="M-10 300 Q160 150 560 140 L560 340 Q300 470 -10 300 Z" fill="url(#team-tones)"/>
      <path d="M-10 300 Q160 150 560 140" fill="none" stroke="var(--blue)" stroke-width="10"/>
      <path d="M-10 300 Q300 470 560 330" fill="none" stroke="var(--blue)" stroke-width="10"/>
    </svg>

    <h1 class="headline">
      <span class="line-1">BETTER</span>
      <span class="line-2">TOGETHER</span>
    </h1>
  </section>

</main>
</body>
</html>
```